IT business looking for Standout Letterhead Design

We need a letterhead design for a company based in Harbor Point, CA called Corvane Systems, Inc. We specialize in IT engineering, installation and technical support pertaining to the department of defense.

We would like to see a design that incorporates the black and gold that matches our company logo.

More information on the company can be found at www.corvane-sys.example

```html
<!DOCTYPE html>
<html lang="en">
<head>
<meta charset="utf-8">
<title>Corvane Systems, Inc. — Letterhead</title>
<link rel="stylesheet" href="https://fonts.googleapis.com/css2?family=Lato:wght@400;700;900&display=swap">
<style>
  :root {
    --backdrop: #e9e9e9;
    --paper: #ffffff;
    --ink: #050708;
    --gold: #e8c21a;
    --gold-deep: #c8921c;
    --ghost: #f3f3f3;
  }
  html, body {
    margin: 0;
    padding: 0;
    width: 1200px;
    height: 1000px;
    overflow: hidden;
    background: var(--backdrop);
    font-family: "Lato", Arial, sans-serif;
  }
  .canvas {
    position: relative;
    width: 1200px;
    height: 1000px;
  }
  .letterhead {
    position: absolute;
    left: 300px;
    top: 78px;
    width: 596px;
    height: 842px;
    background: var(--paper);
    overflow: hidden;
  }
  .letterhead__frame {
    position: absolute;
    inset: 0;
  }
  .brand {
    position: absolute;
    left: 24px;
    top: 80px;
    display: flex;
    align-items: center;
    gap: 6px;
  }
  .brand__dot {
    width: 10px;
    height: 10px;
    border-radius: 50%;
    background: var(--gold-deep);
  }
  .brand__name {
    font-weight: 900;
    font-size: 17px;
    letter-spacing: 0.5px;
    color: var(--ink);
  }
  .contact {
    position: absolute;
    left: 32px;
    top: 127px;
    margin: 0;
    padding: 0;
    list-style: none;
    font-size: 7px;
    font-weight: 700;
    line-height: 8.5px;
    color: var(--ink);
  }
  .contact__item {
    display: flex;
    align-items: center;
    gap: 3px;
    white-space: nowrap;
  }
  .contact__icon {
    width: 6px;
    height: 6px;
    flex: none;
  }
  .ghost-name {
    position: absolute;
    left: 40px;
    top: 640px;
    width: 520px;
    text-align: center;
    font-weight: 900;
    font-size: 78px;
    letter-spacing: 4px;
    color: var(--ghost);
  }
  .footer-web {
    position: absolute;
    left: 50px;
    top: 826px;
    font-size: 7px;
    color: var(--paper);
    letter-spacing: 0.3px;
    white-space: nowrap;
  }
</style>
</head>
<body>
<main class="canvas">
  <section class="letterhead" aria-label="Corvane Systems letterhead">
    <svg class="letterhead__frame" width="596" height="842" viewBox="0 0 596 842" aria-hidden="true">
      <defs>
        <linearGradient id="goldLine" x1="0" y1="0" x2="1" y2="0">
          <stop offset="0" stop-color="#f5e04a"/>
          <stop offset="0.6" stop-color="#e8c21a"/>
          <stop offset="1" stop-color="#c8921c"/>
        </linearGradient>
      </defs>
      <polygon points="197,0 596,0 596,34 440,70 197,0" fill="var(--ink)"/>
      <polyline points="197,1 440,78 596,37" fill="none" stroke="url(#goldLine)" stroke-width="3"/>
      <polygon points="0,842 0,833 87,807 186,842" fill="var(--ink)"/>
      <polyline points="0,828 87,802 186,842" fill="none" stroke="url(#goldLine)" stroke-width="2.5"/>
    </svg>

    <div class="brand">
      <span class="brand__dot"></span>
      <span class="brand__name">CORVANE</span>
    </div>

    <ul class="contact">
      <li class="contact__item">
        <svg class="contact__icon" viewBox="0 0 10 10"><path d="M5 1 L9 5 H8 V9 H2 V5 H1 Z" fill="currentColor"/></svg>
        Corvane Systems, Inc.
      </li>
      <li class="contact__item">
        <svg class="contact__icon" viewBox="0 0 10 10"><path d="M5 1 A3 3 0 0 1 8 4 C8 6 5 9 5 9 C5 9 2 6 2 4 A3 3 0 0 1 5 1 Z" fill="none" stroke="currentColor" stroke-width="1.3"/></svg>
        Harbor Point, CA
      </li>
      <li class="contact__item">
        <svg class="contact__icon" viewBox="0 0 10 10"><path d="M2 1 L4 1 L5 3.5 L3.8 4.5 C4.4 5.8 5 6.4 6 6.8 L7 5.6 L9 6.5 L9 8.5 C5 9 1 5 2 1 Z" fill="none" stroke="currentColor" stroke-width="1.1"/></svg>
        619-555-0142
      </li>
      <li class="contact__item">
        <svg class="contact__icon" viewBox="0 0 10 10"><rect x="1" y="4" width="8" height="5" fill="currentColor"/><rect x="3" y="1" width="4" height="3" fill="currentColor"/></svg>
        619-555-0187
      </li>
      <li class="contact__item">
        <svg class="contact__icon" viewBox="0 0 10 10"><rect x="1" y="2.5" width="8" height="5" fill="currentColor"/><path d="M1 2.5 L5 5.5 L9 2.5" fill="none" stroke="#fff" stroke-width="0.8"/></svg>
        info@corvane-sys.example
      </li>
    </ul>

    <div class="ghost-name" aria-hidden="true">CORVANE</div>

    <div class="footer-web">www.corvane-sys.example</div>
  </section>
</main>
</body>
</html>
```